professional business card design

Business card design. Photos have been uploaded and i am open to the designer choosing which photos to use. Would like the card to be mostyly in a grey scale design with black, whites, silver & grey colours. I have added copy of our flyer as would like on the back side of card our services to be listed. Do not use any bright colurs such as blue red green or yellow. i need to be able to edit the phone number and naem in the final card design submitted.

Target Market(s)

Clients

Industry/Entity Type

earhmovibng and transport

Contact Information for Business Card

Director Name, address, email, phone number and services

Colors

Designer to choose only greyscale colors for use in the design.

Requirements
Should not have
• no yellow, red, blue or green

```html
<!DOCTYPE html>
<html lang="en">
<head>
<meta charset="utf-8">
<title>Granite Haul – Business Card</title>
<link href="https://fonts.googleapis.com/css2?family=Arimo:ital,wght@0,400;0,700;1,400&display=swap" rel="stylesheet">
<style>
  :root {
    --page-bg: #a9a9a9;
    --card-black: #0e0e0e;
    --card-black-2: #222;
    --card-white: #ffffff;
    --ink: #1f1f1f;
    --ink-soft: #3a3a3a;
    --silver: #b9b9b9;
    --silver-dark: #6f6f6f;
    --on-dark: #f2f2f2;
  }
  * { box-sizing: border-box; margin: 0; padding: 0; }
  html, body { width: 1200px; height: 900px; overflow: hidden; }
  body {
    background: var(--page-bg);
    font-family: "Arimo", Arial, sans-serif;
    display: flex; flex-direction: column; align-items: center; justify-content: center;
    gap: 40px;
  }
  .card {
    width: 620px; height: 354px; border-radius: 22px; position: relative; overflow: hidden;
    box-shadow: 0 8px 22px rgba(0,0,0,.28);
  }
  .brand {
    font-weight: 700; letter-spacing: 4px; text-transform: uppercase; white-space: nowrap;
  }

  /* Back */
  .card-back {
    background: radial-gradient(ellipse at 50% 30%, var(--card-black-2), var(--card-black) 70%);
    color: var(--on-dark);
    padding: 28px 40px 0;
    text-align: center;
  }
  .card-back .brand { font-size: 44px; color: var(--silver); line-height: 1; margin-bottom: 14px; }
  .services-title { font-size: 21px; font-weight: 700; letter-spacing: .5px; margin-bottom: 12px; }
  .services {
    display: grid; grid-template-columns: 1fr 1fr; column-gap: 36px; text-align: left;
    font-size: 15px; line-height: 1.32; list-style: none; margin-bottom: 14px;
  }
  .services li::before { content: "●"; font-size: 10px; margin-right: 8px; vertical-align: 2px; }
  .note { font-size: 14px; margin-bottom: 4px; }
  .cta { font-size: 17px; font-weight: 700; }

  /* Front */
  .card-front { background: var(--card-white); color: var(--ink); }
  .card-front .brand {
    position: absolute; top: 30px; right: 34px; font-size: 40px; line-height: 1;
    color: var(--silver-dark); z-index: 1;
  }
  .truck-photo {
    position: absolute; right: 0; top: 100px; width: 240px; height: 254px;
    background: linear-gradient(160deg, #8c8c8c 0%, #cfcfcf 40%, #a3a3a3 70%, #5c5c5c 100%);
  }
  .person { position: absolute; left: 40px; top: 136px; }
  .person-name { font-size: 28px; font-weight: 700; letter-spacing: .5px; line-height: 1.05; white-space: nowrap; }
  .person-role { font-size: 18px; color: var(--ink-soft); }
  .contacts { position: absolute; left: 40px; top: 214px; list-style: none; font-size: 17px; line-height: 1.3; }
  .contacts li { display: flex; align-items: center; gap: 8px; white-space: nowrap; }
  .contacts svg { width: 16px; height: 16px; fill: none; stroke: var(--ink); stroke-width: 2; }
  .address { position: absolute; left: 40px; top: 296px; font-size: 17px; line-height: 1.25; font-style: normal; }
</style>
</head>
<body>

<section class="card card-back">
  <div class="brand">Granite Haul</div>
  <h2 class="services-title">OUR SERVICES</h2>
  <ul class="services">
    <li>Over size loads/hot shot loads</li>
    <li>Road train tippers</li>
    <li>Heavy vehicle recovery services</li>
    <li>Road train tankers</li>
    <li>Potable water deliveries</li>
    <li>Road train flat tops</li>
    <li>Road building/maintenance</li>
    <li>Drop deck trailers</li>
    <li>Earthworks</li>
    <li>Mine site accredited</li>
    <li>Sand &amp; metal supply &amp; cartage</li>
    <li>Equipment &amp; operators</li>
  </ul>
  <p class="note">we offer a large range of services not listed.</p>
  <p class="cta">So call us today for a personalised quote to suit your needs.</p>
</section>

<section class="card card-front">
  <div class="truck-photo" role="img" aria-label="Photo of a heavy haulage prime mover carrying an oversize load"></div>
  <div class="brand">Granite Haul</div>
  <div class="person">
    <h1 class="person-name">MARCUS HALE</h1>
    <p class="person-role">Managing Director</p>
  </div>
  <ul class="contacts">
    <li><svg viewBox="0 0 24 24"><path d="M5 3h4l2 5-3 2a12 12 0 0 0 6 6l2-3 5 2v4a2 2 0 0 1-2 2A17 17 0 0 1 3 5a2 2 0 0 1 2-2z"/></svg>044-987 654 321</li>
    <li><svg viewBox="0 0 24 24"><rect x="3" y="5" width="18" height="14"/><path d="M3 5l9 8 9-8"/></svg>info@granitehaul.com</li>
    <li><svg viewBox="0 0 24 24"><circle cx="12" cy="12" r="9"/><path d="M3 12h18M12 3c3 3 3 15 0 18M12 3c-3 3-3 15 0 18"/></svg>www.granitehaul.com</li>
  </ul>
  <address class="address">421, Address line goes<br>here 45452, Country Name</address>
</section>

</body>
</html>
```